business card deign

Logo needs the following on it.
1. attached logo
2. Tagline - "If it keeps the cooler full or the night rolling...we've got it!"
3. Name- Delia Fenwick, Founder and CPO
4. Address - 418 E. Harlow Avenue, Ste 2204, Tampa, FL. 33719
5. Phone - 720.555.0187

```html
<!DOCTYPE html>
<html lang="en">
<head>
<meta charset="utf-8">
<title>Hopline Business Card</title>
<link href="https://fonts.googleapis.com/css2?family=Poppins:wght@300;400;600;700&display=swap" rel="stylesheet">
<style>
  :root {
    --backdrop: #757a7c;
    --card-white: #ffffff;
    --card-black: #1c1a1b;
    --ink: #1a1819;
    --ink-soft: #3a3839;
    --rule: #4a4849;
    --paper-text: #ffffff;
  }
  * { box-sizing: border-box; margin: 0; padding: 0; }
  html, body {
    width: 1200px; height: 900px; overflow: hidden;
    background: var(--backdrop);
    font-family: "Poppins", sans-serif;
  }
  .canvas {
    width: 1200px; height: 900px;
    display: flex; flex-direction: column;
    align-items: center; justify-content: center; gap: 48px;
  }
  .card {
    position: relative;
    width: 580px; height: 331px;
    overflow: hidden;
    box-shadow: 0 10px 24px rgba(0,0,0,0.28);
  }
  /* Front side */
  .card-front { background: var(--card-white); color: var(--ink); }
  .brand-mark {
    position: absolute; display: flex; align-items: center; gap: 10px;
    font-weight: 700; letter-spacing: 0.3em;
  }
  .card-front .brand-mark { left: 40px; top: 118px; font-size: 18px; color: var(--ink); }
  .brand-dot { width: 12px; height: 12px; border-radius: 50%; background: currentColor; }
  .name-band {
    position: absolute; left: 0; top: 186px;
    width: 262px; height: 34px;
    background: var(--ink);
    clip-path: polygon(0 0, 100% 0, 93% 100%, 0 100%);
    display: flex; align-items: center; padding-left: 40px;
  }
  .person-name {
    color: var(--paper-text); font-weight: 600; font-size: 16px;
    letter-spacing: 0.02em; text-transform: uppercase;
  }
  .person-title {
    position: absolute; left: 40px; top: 230px;
    font-size: 13px; font-weight: 400; letter-spacing: 0.04em;
    text-transform: uppercase; color: var(--ink-soft);
  }
  .divider-rule {
    position: absolute; left: 262px; right: 0; top: 186px;
    height: 1px; background: var(--rule);
  }
  .contact-list {
    position: absolute; right: 24px; top: 204px;
    list-style: none; display: flex; flex-direction: column; gap: 10px;
  }
  .contact-item {
    display: flex; align-items: flex-start; justify-content: flex-end; gap: 10px;
    font-size: 10.5px; line-height: 1.35; text-align: right; color: var(--ink);
  }
  .contact-icon { flex: none; width: 14px; height: 14px; }
  /* Back side */
  .card-back {
    background: var(--card-black); color: var(--paper-text);
    display: flex; flex-direction: column; align-items: center; justify-content: center;
  }
  .card-back .brand-mark {
    position: static; font-size: 34px; letter-spacing: 0.42em;
    margin-right: -0.42em; color: var(--paper-text);
  }
  .tagline {
    margin-top: 22px; font-weight: 300; font-size: 12px;
    letter-spacing: 0.16em; color: var(--paper-text);
    white-space: nowrap;
  }
</style>
</head>
<body>
<main class="canvas">
  <section class="card card-front" aria-label="Business card front">
    <div class="brand-mark"><span class="brand-dot"></span><span>HOPLINE</span></div>
    <div class="name-band"><span class="person-name">Delia Fenwick</span></div>
    <p class="person-title">Founder and CPO</p>
    <div class="divider-rule"></div>
    <ul class="contact-list">
      <li class="contact-item">
        <span>720.555.0187</span>
        <svg class="contact-icon" viewBox="0 0 14 14" aria-hidden="true">
          <circle cx="7" cy="7" r="7" fill="#1a1819"/>
          <path d="M4.6 3.8l1.2-.3.7 1.6-.8.6c.4.9 1 1.5 1.9 1.9l.6-.8 1.6.7-.3 1.2c-2.6.1-5-2.3-4.9-4.9z" fill="#fff"/>
        </svg>
      </li>
      <li class="contact-item">
        <span>418 E. Harlow Avenue, Ste 2204, Tampa,<br>FL. 33719</span>
        <svg class="contact-icon" viewBox="0 0 14 14" aria-hidden="true">
          <circle cx="7" cy="7" r="7" fill="#1a1819"/>
          <path d="M7 3.4a2.3 2.3 0 0 0-2.3 2.3c0 1.7 2.3 4.3 2.3 4.3s2.3-2.6 2.3-4.3A2.3 2.3 0 0 0 7 3.4zm0 3.2a.9.9 0 1 1 0-1.8.9.9 0 0 1 0 1.8z" fill="#fff"/>
        </svg>
      </li>
    </ul>
  </section>

  <section class="card card-back" aria-label="Business card back">
    <div class="brand-mark"><span>HOPLINE</span></div>
    <p class="tagline">"If it keeps the cooler full or the night rolling...we've got it!"</p>
  </section>
</main>
</body>
</html>
```